Brookvale Agribusiness Consulting needs a Website Design.

We need a website design for a new company based in UK. Brookvale offers agribusiness consulting and farm design services to farmers, smallholders and the wider agribusiness industry to assist clients in adopting more sustainable and regenerative production, processing and marketing practices.
Services are offered face-to-face and on a remote platform.
Services are offered in the UK and overseas.
We would like to see designs that reflect the natural environment, business and sustainability. Desired colours; green, blue, grey. The final design should communicate professionalism in the rural economy.
The design should be able to be customized by the client to make future changes and additions.
Target Market(s)
Farmers, smallholders, and the agricultural industry in UK and overseas.
Industry/Entity Type
Agribusiness
Number of Pages Required
4 page
Look and feel
Each slider illustrates characteristics of the customer's brand and the style your logo design should communicate.

```html
<!DOCTYPE html>
<html lang="en">
<head>
<meta charset="utf-8">
<title>Brookvale Agribusiness Consulting</title>
<link rel="stylesheet" href="https://fonts.googleapis.com/css2?family=Roboto:wght@400;500&family=Open+Sans:wght@400;600&family=Oswald:wght@400&family=Lobster&display=swap">
<style>
:root{
  --backdrop:#8fb52a;
  --cream:#fff8d6;
  --green:#7dba2a;
  --green-light:#93cf33;
  --green-dark:#5f9a1e;
  --box-green:#86b92f;
  --amber:#fdb316;
  --ink:#333333;
  --muted:#555555;
  --navy:#1d3a5c;
  --soil:#3a2e22;
  --footer:#0c0c0c;
  --white:#ffffff;
}
*{margin:0;padding:0;box-sizing:border-box}
html,body{width:1200px;height:2250px;overflow:hidden}
body{background:var(--backdrop);font-family:"Open Sans",Arial,sans-serif;color:var(--ink);position:relative}
.page{position:absolute;left:99px;top:58px;width:1002px;height:2128px;background:var(--white)}
.abs{position:absolute}
/* header */
.site-header{left:0;top:0;width:1002px;height:124px;background:var(--cream)}
.brand{left:24px;top:40px;display:flex;align-items:center;gap:12px}
.brand-dot{width:44px;height:44px;border-radius:50%;background:var(--green)}
.brand-name{font-family:"Roboto",sans-serif;font-weight:500;font-size:30px;color:#4a4a3a}
.search{left:543px;top:50px;width:176px;height:36px;background:var(--white);border:1px solid #e6e0c0;border-radius:3px;font-size:12px;color:#555;padding:9px 14px}
.search svg{position:absolute;right:12px;top:11px}
.phone-icon{left:759px;top:45px;width:42px;height:42px;border:1px solid var(--navy);border-radius:50%}
.phone-icon svg{position:absolute;left:12px;top:12px}
.contact{left:816px;top:46px;font-family:"Roboto",sans-serif;color:var(--navy);font-size:16px;line-height:26px}
.contact .mail{font-size:14.5px;padding-left:2px}
/* nav */
.main-nav{left:0;top:124px;width:1002px;height:58px;background:linear-gradient(var(--green-light),var(--green));display:flex}
.main-nav a{display:block;height:58px;line-height:58px;color:var(--white);font-family:"Roboto",sans-serif;font-size:14.5px;text-decoration:none;border-right:1px solid rgba(255,255,255,.25);padding:0 26px}
.main-nav .home{width:92px;background:var(--green-dark);position:relative}
.main-nav .home svg{position:absolute;left:35px;top:20px}
/* hero */
.hero{left:0;top:182px;width:1002px;height:530px;background:linear-gradient(180deg,#4d78b5 0%,#9fb9cf 18%,#d9b24a 28%,#c98a2a 45%,#8aa12c 62%,#4f8a1e 100%)}
.slide-arrow{width:34px;height:34px;border-radius:50%;background:rgba(40,40,40,.45)}
.slide-arrow svg{position:absolute;left:11px;top:10px}
.hero-title{left:557px;top:500px;font-family:"Lobster",cursive;font-size:40px;line-height:50px;color:var(--white);text-shadow:0 2px 4px rgba(0,0,0,.35)}
.hero-text{left:558px;top:555px;width:340px;font-size:12px;line-height:19px;color:var(--white)}
/* audience boxes */
.audience{left:0;top:680px;width:1002px;height:257px}
.aud{position:absolute;top:32px;height:225px;text-align:center;color:var(--white)}
.aud h2{font-family:"Roboto",sans-serif;font-weight:400;font-size:27px;margin-top:6px}
.aud p{font-size:12px;line-height:22px;margin:10px auto 0;width:262px}
.aud .go{width:42px;height:42px;border:2px solid rgba(255,255,255,.6);border-radius:50%;margin:14px auto 0;position:relative}
.aud .go svg{position:absolute;left:14px;top:12px}
/* welcome */
.welcome{left:0;top:937px;width:1002px;height:257px;text-align:center}
.welcome h1{font-family:"Roboto",sans-serif;font-weight:400;font-size:33px;color:var(--ink);margin-top:36px}
.welcome p{font-size:11px;line-height:20px;color:var(--muted);width:860px;margin:14px auto 0}
.btn-more{display:inline-block;margin-top:22px;width:174px;height:50px;line-height:46px;border:2px solid var(--green);border-radius:25px;font-size:18px;color:var(--ink)}
/* services */
.services{left:0;top:1194px;width:1002px;height:574px;background:radial-gradient(ellipse at 50% 40%,#6b5944 0%,var(--soil) 60%,#231b14 100%)}
.services h2{position:absolute;left:24px;top:30px;font-family:"Oswald",sans-serif;font-weight:400;font-size:36px;color:var(--white)}
.services .lead{position:absolute;left:24px;top:80px;width:740px;font-size:12.5px;line-height:22px;color:var(--white)}
.round-arrow{width:34px;height:34px;border-radius:50%;border:1px solid rgba(255,255,255,.6);background:rgba(0,0,0,.25)}
.round-arrow svg{position:absolute;left:11px;top:10px}
.card{position:absolute;top:150px;width:295px;height:350px;background:var(--white);text-align:center}
.card .photo{margin:9px;height:174px}
.card h3{font-family:"Roboto",sans-serif;font-weight:400;font-size:18px;color:var(--ink);margin-top:12px}
.card p{font-size:11px;line-height:20px;color:var(--muted);width:250px;margin:8px auto 0}
.card .more{position:absolute;left:0;bottom:0;width:100%;height:38px;line-height:38px;background:#efefef;font-size:11px;color:#222}
/* news */
.news{left:0;top:1768px;width:1002px;height:288px}
.news h2{position:absolute;left:24px;top:48px;font-family:"Roboto",sans-serif;font-weight:400;font-size:21px;color:var(--ink)}
.news-item{position:absolute;top:97px;width:460px;height:140px}
.news-item .thumb{position:absolute;left:0;top:0;width:139px;height:135px}
.news-item h3{position:absolute;left:162px;top:0;font-family:"Roboto",sans-serif;font-weight:400;font-size:16.5px;color:var(--ink);white-space:nowrap}
.news-item .date{position:absolute;left:162px;top:33px;font-size:12px;color:var(--green)}
.news-item p{position:absolute;left:162px;top:57px;width:290px;font-size:11px;line-height:21px;color:var(--ink)}
/* footer */
.site-footer{left:0;top:2056px;width:1002px;height:72px;background:var(--footer);color:var(--white);font-size:12px}
.site-footer .copy{position:absolute;left:24px;top:28px}
.social{position:absolute;top:23px;width:26px;height:26px;border:1px solid var(--white);border-radius:50%}
.foot-links{position:absolute;right:24px;top:28px;word-spacing:2px}
.foot-links span{margin:0 10px}
</style>
</head>
<body>
<div class="page">
  <header class="site-header abs">
    <div class="brand abs"><span class="brand-dot"></span><span class="brand-name">Brookvale</span></div>
    <div class="search abs">Search
      <svg width="12" height="12" viewBox="0 0 12 12"><circle cx="5" cy="5" r="3.8" fill="none" stroke="#333" stroke-width="1.6"/><line x1="7.8" y1="7.8" x2="11" y2="11" stroke="#333" stroke-width="1.8"/></svg>
    </div>
    <div class="phone-icon abs"><svg width="18" height="18" viewBox="0 0 24 24"><path d="M6.6 10.8a15 15 0 0 0 6.6 6.6l2.2-2.2c.3-.3.7-.4 1-.2 1.1.4 2.3.6 3.6.6.6 0 1 .4 1 1V20c0 .6-.4 1-1 1A17 17 0 0 1 3 4c0-.6.4-1 1-1h3.5c.6 0 1 .4 1 1 0 1.3.2 2.5.6 3.6.1.3 0 .7-.2 1z" fill="#1d3a5c"/></svg></div>
    <div class="contact abs"><div>Ph: (01) 555 0142</div><div class="mail">hello@brookvale-agri.co.uk</div></div>
  </header>

  <nav class="main-nav abs">
    <a class="home" href="#" aria-label="Home"><svg width="22" height="18" viewBox="0 0 22 18"><path d="M11 0 0 9h3v9h6v-6h4v6h6V9h3z" fill="#fff"/></svg></a>
    <a href="#" style="width:128px">ABOUT US</a>
    <a href="#" style="width:166px">OUR SERVICES</a>
    <a href="#" style="width:130px">INDUSTRY</a>
    <a href="#" style="width:190px">REQUEST A QUOTE</a>
    <a href="#" style="border:none">CONTACT US</a>
  </nav>

  <section class="hero abs" role="img" aria-label="Sunlit farm field with round hay bales under a blue sky"></section>
  <div class="slide-arrow abs" style="left:37px;top:439px"><svg width="12" height="14" viewBox="0 0 12 14"><path d="M9 1 3 7l6 6" fill="none" stroke="#fff" stroke-width="2"/></svg></div>
  <div class="slide-arrow abs" style="left:929px;top:439px"><svg width="12" height="14" viewBox="0 0 12 14"><path d="M3 1l6 6-6 6" fill="none" stroke="#fff" stroke-width="2"/></svg></div>
  <div class="hero-title abs">Agribusiness Consulting</div>
  <p class="hero-text abs">Vestibulum quis felis ut enim aliquam iaculis. Nullam pharetra tortor at quam viverra volutpat. Phasellus vel faucibus dolor. Curabitur ac nisi non</p>

  <section class="audience abs">
    <svg class="abs" style="left:0;top:0" width="1002" height="40" viewBox="0 0 1002 40">
      <path d="M0 20 Q167 4 334 18 L334 40 L0 40Z" fill="#86b92f"/>
      <path d="M334 18 Q501 2 668 16 L668 40 L334 40Z" fill="#fdb316"/>
      <path d="M668 16 Q835 2 1002 14 L1002 40 L668 40Z" fill="#86b92f"/>
    </svg>
    <div class="aud" style="left:0;width:334px;background:var(--box-green)">
      <h2>Farmers</h2>
      <p>Lorem ipsum dolor sit amet, consete ctetur adipiscing. Duis eros ligula lacinia quis dignisim atne liquam quis consectetur magna. Lorem ipsum dolor sit amet, consete ctetur</p>
      <div class="go"><svg width="10" height="16" viewBox="0 0 10 16"><path d="M2 2l6 6-6 6" fill="none" stroke="#fff" stroke-width="2"/></svg></div>
    </div>
    <div class="aud" style="left:334px;width:334px;background:var(--amber)">
      <h2>Smallholders</h2>
      <p>Lorem ipsum dolor sit amet, consete ctetur adipiscing. Duis eros ligula lacinia quis dignisim atne liquam quis consectetur magna. Lorem ipsum dolor sit amet, consete ctetur</p>
      <div class="go"><svg width="10" height="16" viewBox="0 0 10 16"><path d="M2 2l6 6-6 6" fill="none" stroke="#fff" stroke-width="2"/></svg></div>
    </div>
    <div class="aud" style="left:668px;width:334px;background:var(--box-green)">
      <h2>Agribusiness Industry</h2>
      <p>Lorem ipsum dolor sit amet, consete ctetur adipiscing. Duis eros ligula lacinia quis dignisim atne liquam quis consectetur magna. Lorem ipsum dolor sit amet, consete ctetur</p>
      <div class="go"><svg width="10" height="16" viewBox="0 0 10 16"><path d="M2 2l6 6-6 6" fill="none" stroke="#fff" stroke-width="2"/></svg></div>
    </div>
  </section>

  <section class="welcome abs">
    <h1>Welcome To Brookvale</h1>
    <p>Lorem ipsum dolor sit amet, consectetur adipiscing elit, sed do eiusmod tempor incididunt ut labore et dolore magna aliqua. Ut enim ad minim veniam, quis nostrud exercitation ullamco laboris nisi ut aliquip ex ea commodo consequat. Duis aute irure dolor in reprehenderit in voluptate velit esse cillum dolore eu fugiat nulla pariatur. Excepteur sint occaecat cupidatat non proident, sunt in culpa qui officia deserunt mollit anim id est laborum</p>
    <span class="btn-more">READ MORE</span>
  </section>

  <section class="services abs" role="img" aria-label="Blurred wooden table with a green leaf behind the services cards">
    <h2>OUR SERVICES</h2>
    <p class="lead">Lorem ipsum dolor sit amet, consectetur adipiscing elit, sed do eiusmod tempor incididunt ut labore et dolore magna aliqua. Ut enim ad minim veniam, quis nostrud exercitation ullamco laboris nisi ut aliquip ex ea commodo consequat.</p>
    <div class="round-arrow abs" style="left:902px;top:53px"><svg width="12" height="14" viewBox="0 0 12 14"><path d="M9 1 3 7l6 6" fill="none" stroke="#fff" stroke-width="2"/></svg></div>
    <div class="round-arrow abs" style="left:940px;top:53px"><svg width="12" height="14" viewBox="0 0 12 14"><path d="M3 1l6 6-6 6" fill="none" stroke="#fff" stroke-width="2"/></svg></div>
    <div class="card" style="left:24px">
      <div class="photo" role="img" aria-label="Wooden farm gate in a green pasture" style="background:linear-gradient(#aab8c4 0%,#d6dbe0 30%,#6f8f4a 55%,#4e6f2e 100%)"></div>
      <h3>Regenerative Production</h3>
      <p>Lorem ipsum dolor sit amet, consectetur adipiscing elit, sed do eiusmod tempor incididunt ut labore et dolore magna aliqua.</p>
      <div class="more">READ MORE &raquo;</div>
    </div>
    <div class="card" style="left:352px">
      <div class="photo" role="img" aria-label="Half green, half tilled field under a blue sky" style="background:linear-gradient(#2f7fd0 0%,#a9d2f0 45%,#5d9a3a 55%,#c8bca4 100%)"></div>
      <h3>Processing</h3>
      <p>Lorem ipsum dolor sit amet, consectetur adipiscing elit, sed do eiusmod tempor incididunt ut labore et dolore magna aliqua.</p>
      <div class="more">READ MORE &raquo;</div>
    </div>
    <div class="card" style="left:681px">
      <div class="photo" role="img" aria-label="Crate of fresh local vegetables beside a chalk sign" style="background:linear-gradient(135deg,#3f6a2a 0%,#c43a2a 40%,#e0a040 70%,#c9b48a 100%)"></div>
      <h3>Marketing Practices</h3>
      <p>Lorem ipsum dolor sit amet, consectetur adipiscing elit, sed do eiusmod tempor incididunt ut labore et dolore magna aliqua.</p>
      <div class="more">READ MORE &raquo;</div>
    </div>
  </section>

  <section class="news abs">
    <h2>LATEST NEWS</h2>
    <article class="news-item" style="left:24px">
      <div class="thumb" role="img" aria-label="Cattle grazing in a green field" style="background:linear-gradient(#7fb0e0 0%,#3f7a2a 35%,#5d8f36 70%,#4a3a2a 100%)"></div>
      <h3>Nulla at diam ornare, aliquam urna vel,</h3>
      <div class="date">FEB 25, 2015</div>
      <p>Nulla at diam ornare, aliquam urna vel, commodo urna. Nam id risus a est luctus consectetur quis eget libero. Suspendisse potenti. Pellentesque habitant morbi tristique senectus et netus</p>
    </article>
    <article class="news-item" style="left:534px">
      <div class="thumb" role="img" aria-label="Round hay bales on a harvested field" style="background:linear-gradient(#c99a5a 0%,#d8b07a 50%,#b88a4a 100%)"></div>
      <h3>Nulla at diam ornare, aliquam urna vel,</h3>
      <div class="date">FEB 25, 2015</div>
      <p>Nulla at diam ornare, aliquam urna vel, commodo urna. Nam id risus a est luctus consectetur quis eget libero. Suspendisse potenti. Pellentesque habitant morbi tristique senectus et netus</p>
    </article>
  </section>

  <footer class="site-footer abs">
    <div class="copy">&copy;2015 Brookvale, All Rights Reserved.</div>
    <span class="social" style="left:441px"></span>
    <span class="social" style="left:476px"></span>
    <span class="social" style="left:510px"></span>
    <div class="foot-links">Home<span>|</span>About<span>|</span>Services<span>|</span>Contacts</div>
  </footer>
</div>
</body>
</html>
```